New Toothpaste brand needs a logo & packaging design

Our company is launching a new toothpaste and is looking for a logo and packaging design. The toothpaste brand is called Brivana. The packaging should have the same design quality as the major international brands, such as Lumora, Lumora Totalcare, Dentiva, Pexolo, Wind-rise, Marvest, etc. The dominant colors for our brand should be hues of blue, similar to other major brands. In addition, there should be a little bit of green to represent the "Fresh Mint Blast" flavor and the "Extracts of Aloe Vera" included in the ingredients.

There are typically 3 unique sides on a toothpaste box:

The face: Repeated on ~3 sides of the 4 faces of the box
The back: The 4th box face has the instructions for use, ingredients, company information, bar code/product info, and some branding elements.
The sides: Usually consisting of just the logo, flavor etc.

Please refer to existing brands such as Lumora, Lumora Total-care, and Dentiva for an example of typical box layout and elements.

Task Details:
Package Dimensions: 180 mm x 48 mm x 28 mm, 100 ml toothpaste tube
Brand Name: Brivana
Description: Fluoride Toothpaste
Flavor: Fresh Mint Blast
5 Actions: Protects against cavities and tartar, freshens breath, whitens teeth, and maintains healthy gums. These actions can also be made into a list like Lumora Total Care or Dentiva Max care. For instance, Strong Teeth, Fresh Breath, Whitening, Healthy Gums, Cavity and Tartar Protection.
Also contains whitening micro particles and extracts of aloe vera which may be highlighted on the package

Overall, the look should be high quality and with the same look and feel as the big brands mentioned previously. We do not have an existing logo for this brand. The face of the package is the most important element as it is often repeated on several sides and on the tube itself.

Please let me know if you have any questions.

I've attached some of our favorite big brand designs below. I would say the Lumora Total Care and Gleam vers

The logos I've seen so far for Brivana, have been a bit too bold. A little bold is okay, but just needs to be moderate. 

I would like the colors to be bright and appealing. I mentioned shades of blue being the major color, but green should also be highlighted as well, perhaps in a 80% blue to 20% green ratio. 

Target Market(s)

adult consumer of toothpaste, both female and male.

Industry/Entity Type

It Company

Requirements
Must have
• A logo with the brand name: Brivana
Description or sub text: Fluoride Toothpaste
Flavor: Fresh Mint Blast
A phrase or list describing the Toothpaste Actions: e.g., Protects against cavities and tartar, freshens breath, whitens teeth, and maintains healthy gums. Or as a list simialr to Lumora Total Care or Dentiva Max Care:
-Anti-cavity
-Anti-tartar
-Fresh breath
-Whitening
-Healthy Gums

Special ingredient of "whitening micro particles: and "extracts of aloe vera", which should also be highlighted.

The color should mostly be shades of blue, with only a little bit of green to accentuate the fresh mint blast flavor and aloe vera

Nice to have
• The design should really look good next to lumora total care, gleam pure, and dentiva max care. These are our favorite designs.
Should not have
• For aloe vera, there is no need to show the plant.

The Brivana logo shouldn't be too Bold. This should be appeal to all consumers, not just men.

```html
<!DOCTYPE html>
<html lang="en">
<head>
<meta charset="utf-8">
<title>Brivana Fluoride Toothpaste – Packaging</title>
<link rel="stylesheet" href="https://fonts.googleapis.com/css2?family=Exo+2:wght@400;600;700&family=Open+Sans:wght@400;600;700&display=swap">
<style>
  :root{
    --navy:#0a2a78;
    --blue:#1546b8;
    --bright:#2f7ae0;
    --glow:#bfe4ff;
    --green:#3fa535;
    --leaf:#5cbf3a;
    --paper:#ffffff;
    --ink:#1d3f8f;
    --line:#9aa9c9;
    --bg:#f4f6f9;
  }
  *{box-sizing:border-box;margin:0;padding:0}
  html,body{width:855px;height:1200px;overflow:hidden;background:var(--bg);font-family:"Open Sans",sans-serif}
  .canvas{position:relative;width:855px;height:1200px}

  /* ---------- tube label ---------- */
  .tube-label{position:absolute;left:178px;top:30px;width:500px;height:180px;background:var(--paper);border:1px solid #d8dde8;overflow:hidden}
  .tube-label__band{position:absolute;inset:0 0 70px 0;background:radial-gradient(ellipse at 40% 55%,var(--glow) 0,var(--bright) 30%,var(--blue) 60%,var(--navy) 100%)}
  .tube-label__swoosh{position:absolute;left:0;top:0;width:500px;height:180px}
  .tube-label .brand{position:absolute;left:60px;top:26px;font:600 62px/1 "Exo 2",sans-serif;color:var(--paper)}
  .tube-label .descriptor{position:absolute;left:64px;top:12px;font:600 11px "Open Sans",sans-serif;color:var(--paper);letter-spacing:.5px}
  .tube-label .mint{position:absolute;right:34px;bottom:10px;width:90px;height:52px;border-radius:40% 50% 45% 55%;background:radial-gradient(circle at 40% 40%,var(--leaf),var(--green))}
  .tube-label .flavor{position:absolute;right:140px;bottom:22px;font:700 12px "Open Sans",sans-serif;color:var(--green)}

  /* ---------- front face (native 610 x 163) ---------- */
  .face{position:absolute;width:610px;height:163px;overflow:hidden;background:var(--paper)}
  .face__bg{position:absolute;left:0;top:0;width:470px;height:128px;background:radial-gradient(ellipse at 42% 48%,#fff 0,var(--glow) 8%,var(--bright) 32%,var(--blue) 58%,var(--navy) 100%)}
  .face__art{position:absolute;left:0;top:0;width:610px;height:163px}
  .face .descriptor{position:absolute;left:100px;top:16px;font:600 10px "Open Sans",sans-serif;color:var(--paper);letter-spacing:.6px}
  .face .brand{position:absolute;left:86px;top:30px;font:600 66px/1 "Exo 2",sans-serif;color:var(--paper)}
  .face .volume{position:absolute;left:520px;top:34px;font:700 14px "Open Sans",sans-serif;color:var(--ink)}
  .face .mint{position:absolute;left:500px;top:62px;width:86px;height:50px;border-radius:45% 55% 40% 60%;background:radial-gradient(circle at 40% 40%,var(--leaf),var(--green))}
  .face .flavor{position:absolute;left:488px;top:128px;font:700 10px "Open Sans",sans-serif;color:var(--green)}
  .benefits{position:absolute;left:16px;top:136px;display:flex;gap:22px;list-style:none}
  .benefits li{display:flex;align-items:center;gap:5px;font:600 8.5px "Open Sans",sans-serif;color:var(--ink)}
  .benefits svg{width:10px;height:10px}

  .face--hero{left:38px;top:250px;transform:scale(1.279);transform-origin:0 0;box-shadow:0 2px 6px rgba(10,42,120,.15)}

  /* ---------- dieline ---------- */
  .dieline{position:absolute;left:0;top:0;width:855px;height:1200px}
  .dieline .face{left:122px}
  .cut{position:absolute;border:1px solid var(--line);background:var(--paper)}
  .side-panel{position:absolute;left:122px;width:610px;height:95px;overflow:hidden;background:radial-gradient(ellipse at 40% 50%,var(--glow) 0,var(--bright) 30%,var(--blue) 60%,var(--navy) 100%)}
  .side-panel .brand{position:absolute;left:150px;top:18px;font:600 52px/1 "Exo 2",sans-serif;color:var(--paper)}
  .side-panel .flavor{position:absolute;right:24px;bottom:14px;font:700 10px "Open Sans",sans-serif;color:var(--paper)}
  .back-panel{position:absolute;left:122px;width:610px;height:150px;background:var(--paper);border:1px solid var(--line)}
  .back-panel .info{position:absolute;left:22px;top:14px;width:360px;height:120px;border:1px solid var(--blue)}
  .back-panel .info span{position:absolute;left:14px;right:14px;height:1px;background:var(--line)}
  .back-panel .aside{position:absolute;left:400px;top:14px;width:190px;height:120px;border:1px solid var(--blue)}
  .end-panel{position:absolute;width:92px;height:163px;overflow:hidden;background:radial-gradient(ellipse at 50% 45%,var(--glow) 0,var(--bright) 35%,var(--blue) 65%,var(--navy) 100%);border:1px solid var(--line)}
  .end-panel .brand{position:absolute;left:50%;top:50%;transform:translate(-50%,-50%) rotate(-90deg);font:600 30px/1 "Exo 2",sans-serif;color:var(--paper);white-space:nowrap}
</style>
</head>
<body>
<main class="canvas">

  <!-- tube label -->
  <section class="tube-label" aria-label="Tube label">
    <div class="tube-label__band"></div>
    <svg class="tube-label__swoosh" viewBox="0 0 500 180" aria-hidden="true">
      <path d="M0 120 C160 95 330 120 500 80 L500 112 C330 140 160 118 0 140 Z" fill="#fff"/>
      <path d="M0 122 C160 98 330 118 500 84" fill="none" stroke="#3fa535" stroke-width="3"/>
    </svg>
    <span class="descriptor">Fluoride Toothpaste</span>
    <span class="brand">Brivana</span>
    <span class="flavor">Fresh Mint Blast</span>
    <div class="mint" role="img" aria-label="Fresh mint leaves"></div>
  </section>

  <!-- hero front face -->
  <article class="face face--hero" aria-label="Box front">
    <div class="face__bg"></div>
    <svg class="face__art" viewBox="0 0 610 163" aria-hidden="true">
      <path d="M440 0 C470 40 480 90 458 128 L470 128 C494 88 486 40 458 0 Z" fill="#3fa535"/>
      <path d="M0 128 L610 128" stroke="#3fa535" stroke-width="2"/>
    </svg>
    <span class="descriptor">Fluoride Toothpaste</span>
    <span class="brand">Brivana</span>
    <span class="volume">100ml</span>
    <div class="mint" role="img" aria-label="Fresh mint leaves"></div>
    <span class="flavor">Fresh Mint Blast</span>
    <ul class="benefits">
      <li><svg viewBox="0 0 10 10"><rect x=".5" y=".5" width="9" height="9" fill="none" stroke="#1546b8"/><path d="M2 5 L4 7 L8 2" fill="none" stroke="#3fa535" stroke-width="1.5"/></svg>Anti-cavity</li>
      <li><svg viewBox="0 0 10 10"><rect x=".5" y=".5" width="9" height="9" fill="none" stroke="#1546b8"/><path d="M2 5 L4 7 L8 2" fill="none" stroke="#3fa535" stroke-width="1.5"/></svg>Anti-tartar</li>
      <li><svg viewBox="0 0 10 10"><rect x=".5" y=".5" width="9" height="9" fill="none" stroke="#1546b8"/><path d="M2 5 L4 7 L8 2" fill="none" stroke="#3fa535" stroke-width="1.5"/></svg>Fresh breath</li>
      <li><svg viewBox="0 0 10 10"><rect x=".5" y=".5" width="9" height="9" fill="none" stroke="#1546b8"/><path d="M2 5 L4 7 L8 2" fill="none" stroke="#3fa535" stroke-width="1.5"/></svg>Whitening</li>
      <li><svg viewBox="0 0 10 10"><rect x=".5" y=".5" width="9" height="9" fill="none" stroke="#1546b8"/><path d="M2 5 L4 7 L8 2" fill="none" stroke="#3fa535" stroke-width="1.5"/></svg>Healthy Gums</li>
    </ul>
  </article>

  <!-- dieline -->
  <section class="dieline" aria-label="Box dieline">
    <svg style="position:absolute;left:0;top:0" width="855" height="1200" aria-hidden="true">
      <path d="M140 555 L160 528 L694 528 L714 555" fill="#fff" stroke="#9aa9c9"/>
      <path d="M140 1178 L160 1196 L694 1196 L714 1178" fill="#fff" stroke="#9aa9c9"/>
      <path d="M30 575 L30 705 L20 705 L20 575 Z" fill="#fff" stroke="#9aa9c9"/>
      <path d="M824 575 L824 705 L834 705 L834 575 Z" fill="#fff" stroke="#9aa9c9"/>
    </svg>

    <div class="end-panel" style="left:30px;top:556px"><span class="brand">Brivana</span></div>
    <div class="end-panel" style="left:732px;top:556px"><span class="brand">Brivana</span></div>

    <article class="face" style="top:556px" aria-label="Front panel">
      <div class="face__bg"></div>
      <svg class="face__art" viewBox="0 0 610 163" aria-hidden="true">
        <path d="M440 0 C470 40 480 90 458 128 L470 128 C494 88 486 40 458 0 Z" fill="#3fa535"/>
        <path d="M0 128 L610 128" stroke="#3fa535" stroke-width="2"/>
      </svg>
      <span class="descriptor">Fluoride Toothpaste</span>
      <span class="brand">Brivana</span>
      <span class="volume">100ml</span>
      <div class="mint" role="img" aria-label="Fresh mint leaves"></div>
      <span class="flavor">Fresh Mint Blast</span>
      <ul class="benefits">
        <li>✓ Anti-cavity</li><li>✓ Anti-tartar</li><li>✓ Fresh breath</li><li>✓ Whitening</li><li>✓ Healthy Gums</li>
      </ul>
    </article>

    <div class="side-panel" style="top:719px">
      <span class="brand">Brivana</span>
      <span class="flavor">Fresh Mint Blast</span>
    </div>

    <article class="face" style="top:814px" aria-label="Front panel">
      <div class="face__bg"></div>
      <svg class="face__art" viewBox="0 0 610 163" aria-hidden="true">
        <path d="M440 0 C470 40 480 90 458 128 L470 128 C494 88 486 40 458 0 Z" fill="#3fa535"/>
        <path d="M0 128 L610 128" stroke="#3fa535" stroke-width="2"/>
      </svg>
      <span class="descriptor">Fluoride Toothpaste</span>
      <span class="brand">Brivana</span>
      <span class="volume">100ml</span>
      <div class="mint" role="img" aria-label="Fresh mint leaves"></div>
      <span class="flavor">Fresh Mint Blast</span>
      <ul class="benefits">
        <li>✓ Anti-cavity</li><li>✓ Anti-tartar</li><li>✓ Fresh breath</li><li>✓ Whitening</li><li>✓ Healthy Gums</li>
      </ul>
    </article>

    <div class="back-panel" style="top:1000px">
      <div class="info">
        <span style="top:30px"></span><span style="top:60px"></span><span style="top:90px"></span>
      </div>
      <div class="aside"></div>
    </div>
  </section>

</main>
</body>
</html>
```